Business Card Design

We are a residential half way house for the addict ,the alcoholic and dual diagnosed in recovery.
i house both men and woman age 18+

Industry/Entity Type

Residential

```html
<!DOCTYPE html>
<html lang="en">
<head>
<meta charset="utf-8">
<title>Meadowlight Family Sober House – Business Card</title>
<link rel="stylesheet" href="https://fonts.googleapis.com/css2?family=Arimo:wght@400;700&family=Questrial&display=swap">
<style>
  :root {
    --backdrop: #d9dadb;
    --card: #ffffff;
    --green: #3fae2a;
    --ink: #2b2b2b;
    --ink-soft: #3a3a3a;
    --white: #ffffff;
  }
  * { box-sizing: border-box; margin: 0; padding: 0; }
  html, body {
    width: 1200px;
    height: 873px;
    overflow: hidden;
    background: var(--backdrop);
  }
  .card {
    position: absolute;
    left: 100px;
    top: 162px;
    width: 1000px;
    height: 548px;
    background: var(--card);
    box-shadow: 0 6px 24px rgba(0, 0, 0, 0.18);
  }
  .brand {
    position: absolute;
    left: 40px;
    top: 120px;
    width: 400px;
    display: flex;
    flex-direction: column;
    align-items: center;
  }
  .brand-dot {
    width: 90px;
    height: 90px;
    border-radius: 50%;
    background: var(--green);
    margin-bottom: 34px;
  }
  .brand-name {
    font-family: "Arimo", sans-serif;
    font-weight: 700;
    font-size: 28px;
    line-height: 1.25;
    color: var(--ink);
    text-align: center;
  }
  .holder {
    position: absolute;
    left: 496px;
    top: 78px;
    font-family: "Arimo", sans-serif;
    font-weight: 700;
    color: var(--ink);
  }
  .holder-name { font-size: 32px; line-height: 1.2; }
  .holder-role { font-size: 23px; line-height: 1.45; margin-top: 4px; }
  .holder-note { font-size: 21px; line-height: 1.4; }
  .contacts {
    position: absolute;
    left: 496px;
    top: 262px;
    list-style: none;
    font-family: "Questrial", sans-serif;
    font-size: 24px;
    color: var(--ink-soft);
  }
  .contact {
    display: flex;
    align-items: center;
    height: 34px;
    margin-bottom: 28px;
  }
  .contact-icon {
    width: 32px;
    height: 32px;
    margin-right: 20px;
    flex: none;
  }
  .info-band {
    position: absolute;
    left: 22px;
    right: 0;
    top: 470px;
    height: 52px;
    display: flex;
    align-items: stretch;
    font-family: "Arimo", sans-serif;
    font-size: 24px;
    color: var(--white);
  }
  .band-pin {
    width: 60px;
    background: var(--green);
    border-radius: 26px 0 0 26px;
    display: flex;
    align-items: center;
    justify-content: center;
  }
  .band-segment {
    background: var(--green);
    display: flex;
    align-items: center;
    white-space: nowrap;
  }
  .band-address {
    margin-left: 8px;
    padding: 0 20px 0 18px;
    border-radius: 0 26px 26px 0;
  }
  .band-tagline {
    margin-left: 8px;
    padding-left: 14px;
    flex: 1;
    border-radius: 26px 0 0 26px;
  }
</style>
</head>
<body>
  <article class="card">
    <div class="brand">
      <div class="brand-dot"></div>
      <div class="brand-name">MEADOWLIGHT FAMILY<br>Sober House Inc.</div>
    </div>

    <header class="holder">
      <div class="holder-name">Dana Whitfield</div>
      <div class="holder-role">Owner</div>
      <div class="holder-note">(15 yrs.in recovery)</div>
    </header>

    <ul class="contacts">
      <li class="contact">
        <svg class="contact-icon" viewBox="0 0 32 32" aria-hidden="true">
          <circle cx="16" cy="16" r="16" fill="var(--green)"/>
          <path d="M11 8.5l3 3.2-1.7 2.3c1 2.3 2.6 3.9 4.9 4.9l2.3-1.7 3.2 3-1.6 2.8c-6.5-.5-11.7-5.7-12.2-12.2z" fill="var(--white)"/>
        </svg>
        <span>(555) 014-0305/ (555) 014-0306</span>
      </li>
      <li class="contact">
        <svg class="contact-icon" viewBox="0 0 32 32" aria-hidden="true">
          <circle cx="16" cy="16" r="16" fill="var(--green)"/>
          <rect x="11" y="8" width="10" height="6" fill="var(--white)"/>
          <rect x="8" y="13" width="16" height="8" rx="1.5" fill="var(--white)"/>
          <rect x="11" y="18" width="10" height="6" fill="var(--white)" stroke="var(--green)" stroke-width="1.2"/>
        </svg>
        <span>(555) 014-5536</span>
      </li>
      <li class="contact">
        <svg class="contact-icon" viewBox="0 0 32 32" aria-hidden="true">
          <circle cx="16" cy="16" r="16" fill="var(--green)"/>
          <rect x="8" y="10" width="16" height="12" rx="1" fill="var(--white)"/>
          <path d="M8.5 10.5l7.5 6 7.5-6" fill="none" stroke="var(--green)" stroke-width="1.6"/>
        </svg>
        <span>danawhitfield@example.com</span>
      </li>
    </ul>

    <footer class="info-band">
      <div class="band-pin">
        <svg width="26" height="30" viewBox="0 0 26 30" aria-hidden="true">
          <circle cx="13" cy="15" r="13" fill="var(--white)"/>
          <path d="M13 6a6 6 0 0 0-6 6c0 4.5 6 11 6 11s6-6.5 6-11a6 6 0 0 0-6-6z" fill="var(--green)"/>
          <circle cx="13" cy="12" r="2.3" fill="var(--white)"/>
        </svg>
      </div>
      <div class="band-segment band-address">4720 Palmetto Ln. Harbor Vale, Fla 33400</div>
      <div class="band-segment band-tagline">Family friendly environment</div>
    </footer>
  </article>
</body>
</html>
```